Bluefern Realty Letterhead

Bluefern Realty Guan
417 Corrin Tide Avenue, Ste B305
Marbo Cove, GU. 96921

Industry/Entity Type

Real Estate

Font styles to use
Serif

Colors

Designer to choose colors to be used in the design.

```html
<!DOCTYPE html>
<html lang="en">
<head>
<meta charset="utf-8">
<title>Bluefern Realty Letterhead</title>
<link rel="stylesheet" href="https://fonts.googleapis.com/css2?family=Montserrat:wght@400;600&family=PT+Sans&display=swap">
<style>
  :root {
    --backdrop: #e9eaec;
    --paper: #ffffff;
    --ink: #1f1f1f;
    --brand-blue: #1b96d4;
    --brand-light: #4fc0e8;
    --brand-sun: #f7b040;
  }
  * { margin: 0; padding: 0; box-sizing: border-box; }
  html, body {
    width: 1200px; height: 900px; overflow: hidden;
    background: var(--backdrop);
  }
  .letterhead {
    position: absolute; left: 260px; top: 10px;
    width: 680px; height: 880px;
    background: var(--paper);
    color: var(--ink);
    font-family: "Montserrat", sans-serif;
    overflow: hidden;
  }
  .brand {
    position: absolute; right: 49px; top: 92px;
    width: 230px; text-align: center;
  }
  .brand-mark {
    display: block; width: 14px; height: 14px; border-radius: 50%;
    background: var(--brand-sun); margin: 0 auto 12px;
  }
  .brand-name {
    font-family: "Montserrat", sans-serif; font-weight: 400;
    font-size: 18px; letter-spacing: 1.5px; color: var(--brand-light);
    text-transform: uppercase; line-height: 1.2; white-space: nowrap;
  }
  .letter {
    position: absolute; left: 49px; width: 583px;
  }
  .date, .salutation, .closing, .signer {
    font-weight: 600; font-size: 11px; letter-spacing: 0.6px;
  }
  .date { top: 185px; }
  .salutation { top: 216px; }
  .body { top: 260px; }
  .body p {
    font-size: 10.8px; line-height: 16.7px; letter-spacing: 0.72px;
    text-align: justify; margin-bottom: 16.7px;
  }
  .closing { top: 586px; }
  .signature {
    top: 615px; width: 200px; height: 42px;
    background: linear-gradient(90deg, #ececec, #f6f6f6);
  }
  .signer { top: 679px; }
  .address {
    position: absolute; left: 49px; top: 818px;
    font-family: "PT Sans", sans-serif; font-style: normal;
    font-size: 11px; line-height: 18px;
  }
  .decoration {
    position: absolute; left: 300px; top: 720px;
    width: 380px; height: 160px;
    background: linear-gradient(135deg, rgba(27,150,212,0.35) 0%, rgba(27,150,212,0.55) 65%, rgba(247,176,64,0.55) 100%);
  }
</style>
</head>
<body>
  <article class="letterhead">
    <header class="brand">
      <span class="brand-mark"></span>
      <div class="brand-name">Bluefern Realty</div>
    </header>

    <p class="letter date">Monday, January 05, 2023</p>
    <p class="letter salutation">Dear Madam/Sir</p>

    <section class="letter body">
      <p>Lorem ipsum dolor sit amet, consectetur adipiscing elit, sed do eiusmod tempor incididunt ut labore et dolore magna aliqua. Ut enim ad minim veniam, quis nostrud exercitation ullamco laboris nisi ut aliquip ex ea commodo consequat. Duis aute irure dolor in reprehenderit in voluptate velit esse cillum dolore eu fugiat nulla pariatur. Excepteur sint occaecat cupidatat non proident, sunt in culpa qui officia deserunt mollit anim id est laborum.</p>
      <p>Curabitur pretium tincidunt lacus. Nulla gravida orci a odio. Nullam varius, turpis et commodo pharetra, est eros bibendum elit, nec luctus magna felis sollicitudin mauris. Integer in mauris eu nibh euismod gravida. Duis ac tellus et risus vulputate vehicula. Donec lobortis risus a elit. Etiam tempor. Ut ullamcorper, ligula eu tempor congue, eros est euismod turpis, id tincidunt sapien risus a quam. Maecenas fermentum consequat mi. Donec fermentum.</p>
      <p>Pellentesque malesuada nulla a mi. Duis sapien sem, aliquet nec, commodo eget, consequat quis, neque. Aliquam faucibus, elit ut dictum aliquet, felis nisl adipiscing sapien, sed malesuada diam lacus eget erat. Cras mollis scelerisque nunc. Nullam arcu. Aliquam consequat. Curabitur augue lorem, dapibus quis, laoreet et, pretium ac, nisi. Aenean magna nisl, mollis quis, molestie eu, feugiat in, orci. In hac habitasse platea dictumst.</p>
    </section>

    <p class="letter closing">Sincerely,</p>
    <div class="letter signature" role="img" aria-label="Handwritten signature of the sender"></div>
    <p class="letter signer">Mr. Talen Ruvek</p>

    <address class="address">
      417 Corrin Tide Avenue, Ste B305<br>
      Marbo Cove, GU. 96921
    </address>

    <div class="decoration" role="img" aria-label="Decorative coastal emblem in blue and orange"></div>
  </article>
</body>
</html>
```